Mobile Friendly Lead Generation Landing Page

We are a web marketing company that specialized in web lead generation. Recently we have started buying media from mobile devices and we need a mobile interface(landing page) where we can collect user data in an effective manner.

Our current mobile landing page is:
http://www.pathwaylocate.example.com/lp13d/index.aspx?a=true&source=591483
Through this you can see what the steps/questions users need to answer to get matched to a school. We need the design for the whole process.

We are pretty open for design ideas and our goal is to make this mobile optimized landing page have the look and feel of an app...but not an app.
There are several questions in the process but we are open to changing the way they are presented. As in, you can have one question at a time or a few.
The goal is to make this EXTREMELY EASY for users to interact with.

One example that we have liked is:
http://tutorhubnet.example.com/schools/72615-page1.thub (please note that this opens only on mobile devices)

Some of these screenshots are attached.

Our web form looks like this:
http://www.pathwaylocate.example.com/lp88/index.aspx?a=true

```html
<!DOCTYPE html>
<html lang="en">
<head>
<meta charset="utf-8">
<title>3 Minute Form – School Question</title>
<link href="https://fonts.googleapis.com/css2?family=Roboto:wght@300;400;500&display=swap" rel="stylesheet">
<style>
  :root {
    --stage: #eceef1;
    --page-green: #84d60a;
    --page-green-deep: #78c808;
    --back-green: #5fa204;
    --card: #ffffff;
    --ink: #2b2b2b;
    --blue: #1a8ff0;
    --button-blue: #0d97f7;
    --track: #e6e9ec;
    --option-border: #e3e5e8;
    --option-icon: #8e8e8e;
    --option-label: #7a7a7a;
    --tab-text: #8fb35a;
  }
  * { box-sizing: border-box; margin: 0; padding: 0; }
  html, body {
    width: 923px; height: 1200px; overflow: hidden;
    background: var(--stage);
    font-family: "Roboto", Arial, sans-serif;
  }
  .screen {
    position: absolute; left: 161px; top: 132px;
    width: 600px; height: 936px;
    background: var(--page-green);
    overflow: hidden;
  }
  .star-pattern {
    position: absolute; inset: 0;
    background: linear-gradient(180deg, var(--page-green) 0%, var(--page-green-deep) 100%);
  }
  .form-title {
    position: absolute; top: 40px; left: 0; right: 0;
    text-align: center; font-weight: 300; font-size: 39px;
    color: var(--ink); letter-spacing: -0.5px;
  }
  .form-title strong { font-weight: 500; }
  .progress-tab {
    position: absolute; top: 124px; left: 236px;
    width: 132px; height: 22px;
    background: var(--card); border-radius: 14px 14px 0 0;
    font-size: 10px; text-align: center; line-height: 24px;
    color: var(--tab-text); letter-spacing: 0.5px;
  }
  .form-card {
    position: absolute; top: 142px; left: 20px;
    width: 562px; height: 544px;
    background: var(--card); border-radius: 4px 4px 0 0;
  }
  .progress {
    position: absolute; top: 16px; left: 18px; right: 18px; height: 8px;
  }
  .progress-track { position: absolute; top: 3px; height: 3px; background: var(--track); }
  .progress-fill {
    position: absolute; top: 2px; left: 0; width: 96px; height: 5px;
    background: var(--blue); border-radius: 3px;
  }
  .progress-step {
    position: absolute; top: 1px; left: 104px; width: 14px; height: 7px;
    background: var(--blue); border-radius: 4px;
  }
  .progress-dot {
    position: absolute; top: -3px; left: 120px; width: 15px; height: 15px;
    background: var(--blue); border-radius: 50%;
  }
  .question {
    position: absolute; top: 68px; left: 0; right: 0;
    text-align: center; font-weight: 400; font-size: 39px;
    color: var(--blue); letter-spacing: -0.3px;
  }
  .option {
    position: absolute; top: 152px; width: 235px; height: 177px;
    border: 2px solid var(--option-border); border-radius: 4px;
    display: flex; flex-direction: column; align-items: center;
    padding-top: 38px;
  }
  .option--yes { left: 29px; }
  .option--no { left: 298px; }
  .option svg { width: 52px; height: 52px; }
  .option-label {
    margin-top: 18px; font-size: 27px; font-weight: 300;
    color: var(--option-label);
  }
  .next-button {
    position: absolute; top: 385px; left: 29px;
    width: 504px; height: 104px;
    background: var(--button-blue); border-radius: 5px;
    color: #fff; font-size: 36px; font-weight: 400;
    display: flex; align-items: center; justify-content: center; gap: 18px;
  }
  .next-button svg { width: 16px; height: 28px; }
  .back-bar {
    position: absolute; top: 686px; left: 20px;
    width: 562px; height: 71px;
    background: var(--back-green); border-radius: 0 0 4px 4px;
    color: #fff; font-size: 22px; font-weight: 300;
    display: flex; align-items: center; justify-content: center; gap: 8px;
  }
  .back-bar svg { width: 9px; height: 16px; }
</style>
</head>
<body>
  <main class="screen">
    <div class="star-pattern" role="img" aria-label="Faint star pattern on green background"></div>

    <h1 class="form-title">Fill out our <strong>3 Minute</strong> form!</h1>

    <div class="progress-tab">PROGRESS:</div>

    <section class="form-card">
      <div class="progress" aria-label="Form progress">
        <div class="progress-track" style="left:0; width:380px;"></div>
        <div class="progress-track" style="left:390px; right:0;"></div>
        <div class="progress-fill"></div>
        <div class="progress-step"></div>
        <div class="progress-dot"></div>
      </div>

      <h2 class="question">Are you currently in school?</h2>

      <div class="option option--yes">
        <svg viewBox="0 0 52 52" aria-hidden="true">
          <polyline points="6,27 20,41 46,10" fill="none" stroke="var(--option-icon)" stroke-width="5" stroke-linecap="round" stroke-linejoin="round"/>
        </svg>
        <span class="option-label">YES</span>
      </div>

      <div class="option option--no">
        <svg viewBox="0 0 52 52" aria-hidden="true">
          <path d="M10 10 L42 42 M42 10 L10 42" stroke="var(--option-icon)" stroke-width="5" stroke-linecap="round"/>
        </svg>
        <span class="option-label">NO</span>
      </div>

      <div class="next-button">
        Next
        <svg viewBox="0 0 16 28" aria-hidden="true">
          <polyline points="3,3 13,14 3,25" fill="none" stroke="#fff" stroke-width="3" stroke-linecap="round" stroke-linejoin="round"/>
        </svg>
      </div>
    </section>

    <div class="back-bar">
      <svg viewBox="0 0 9 16" aria-hidden="true">
        <polyline points="7,2 2,8 7,14" fill="none" stroke="#fff" stroke-width="2" stroke-linecap="round" stroke-linejoin="round"/>
      </svg>
      Back
    </div>
  </main>
</body>
</html>
```